Vesit cards for web development company

We need a business card design for our company. The company develops online platforms and conducts marketing consulting. Company logo. The cards must fit in with us (a junior start UP), but they must also be professional enough to impress with investors like banks. We wish you a combination of classic and modern design

Target Market(s)

Business partners and IT and marketing customers

Industry/Entity Type

It Company

Contact Information for Business Card

Folgende Information müssen Drauf.
Name, Position, Telefon Nr., Mobile Nr., E-Mail adresse, Optional sind noch Webadresse und HRB Nummer

Colors

Designer to choose colors to be used in the design.

Requirements
Must have
• The cards have to fit into the logo later and have to be dynamic and serious at the same time

```html
<!DOCTYPE html>
<html lang="en">
<head>
<meta charset="UTF-8">
<title>Brightpath Business Card</title>
<link href="https://fonts.googleapis.com/css2?family=Montserrat:wght@600;700&family=Roboto:wght@400;500&display=swap" rel="stylesheet">
<style>
  :root {
    --brand-blue: #1e76c0;
    --brand-grey: #939597;
    --fold-grey: #6e7073;
    --ink: #222425;
    --paper: #ffffff;
    --stage-top: #6f777c;
    --stage-bottom: #3f4549;
  }
  * { margin: 0; padding: 0; box-sizing: border-box; }
  html, body { width: 1200px; height: 900px; overflow: hidden; }
  body {
    background: radial-gradient(ellipse at 55% 40%, var(--stage-top), var(--stage-bottom));
    font-family: "Roboto", Arial, sans-serif;
    position: relative;
  }
  .card {
    position: absolute;
    width: 520px;
    height: 300px;
    border-radius: 18px;
    overflow: hidden;
    box-shadow: 0 14px 30px rgba(0,0,0,0.35);
  }
  .card-front { left: 50px; top: 300px; background: var(--brand-blue); }
  .card-back { left: 630px; top: 300px; background: var(--paper); }

  .brand {
    position: absolute;
    display: flex;
    align-items: center;
    gap: 14px;
    font-family: "Montserrat", Arial, sans-serif;
    font-weight: 700;
    letter-spacing: 2px;
    white-space: nowrap;
  }
  .card-front .brand {
    left: 50%; top: 50%;
    transform: translate(-50%, -50%);
    color: var(--paper);
    font-size: 44px;
  }
  .card-front .brand-mark { width: 34px; height: 34px; border-radius: 50%; background: var(--paper); }

  .card-back .brand { left: 34px; top: 34px; color: var(--brand-blue); font-size: 28px; }
  .card-back .brand-mark { width: 22px; height: 22px; border-radius: 50%; background: var(--brand-blue); }

  .back-shapes { position: absolute; inset: 0; }

  .contact-list {
    position: absolute;
    left: 34px; top: 112px;
    list-style: none;
    font-size: 13px;
    color: var(--ink);
  }
  .contact-list li { display: flex; align-items: center; gap: 10px; height: 24px; white-space: nowrap; }
  .contact-icon { width: 16px; height: 16px; flex: none; }

  .name-band {
    position: absolute;
    left: 318px; top: 46px;
    width: 202px; height: 62px;
    color: var(--paper);
    text-align: center;
    padding-top: 12px;
  }
  .person-name { font-size: 18px; font-weight: 400; letter-spacing: 1px; white-space: nowrap; }
  .person-role { font-size: 10px; letter-spacing: 1px; margin-top: 3px; }

  .address {
    position: absolute;
    left: 290px; top: 200px;
    width: 220px;
    color: var(--paper);
    font-size: 13px;
    line-height: 1.5;
    text-align: center;
  }
</style>
</head>
<body>

  <section class="card card-front">
    <div class="brand"><span class="brand-mark"></span><span class="brand-name">BRIGHTPATH</span></div>
  </section>

  <section class="card card-back">
    <svg class="back-shapes" viewBox="0 0 520 300" width="520" height="300" aria-hidden="true">
      <polygon points="360,0 520,0 520,300 150,300" fill="var(--brand-blue)"/>
      <polygon points="318,46 520,46 520,108 318,108" fill="var(--brand-grey)"/>
      <polygon points="318,46 345,30 345,46" fill="var(--fold-grey)"/>
    </svg>

    <div class="brand"><span class="brand-mark"></span><span class="brand-name">BRIGHTPATH</span></div>

    <ul class="contact-list">
      <li>
        <svg class="contact-icon" viewBox="0 0 16 16"><rect width="16" height="16" rx="2" fill="var(--brand-blue)"/><path d="M5 3.5l2 2-1 1.3c.6 1.3 1.6 2.3 2.9 2.9l1.3-1 2 2-1.2 1.6C7.6 12 4 8.4 3.6 4.7z" fill="#fff"/></svg>
        <span>555-014-2870</span>
      </li>
      <li>
        <svg class="contact-icon" viewBox="0 0 16 16"><rect width="16" height="16" rx="2" fill="var(--brand-blue)"/><rect x="5" y="3" width="6" height="10" rx="1" fill="none" stroke="#fff" stroke-width="1.3"/><circle cx="8" cy="11.2" r=".7" fill="#fff"/></svg>
        <span>555-019-3346</span>
      </li>
      <li>
        <svg class="contact-icon" viewBox="0 0 16 16"><rect width="16" height="16" rx="2" fill="var(--brand-blue)"/><rect x="3" y="4.5" width="10" height="7" fill="none" stroke="#fff" stroke-width="1.2"/><path d="M3 4.5l5 4 5-4" fill="none" stroke="#fff" stroke-width="1.2"/></svg>
        <span>hello@brightpath.io</span>
      </li>
      <li>
        <svg class="contact-icon" viewBox="0 0 16 16"><rect width="16" height="16" rx="2" fill="var(--brand-blue)"/><circle cx="8" cy="8" r="4.5" fill="none" stroke="#fff" stroke-width="1.2"/><path d="M3.5 8h9M8 3.5c-2 2.5-2 6.5 0 9M8 3.5c2 2.5 2 6.5 0 9" fill="none" stroke="#fff" stroke-width="1"/></svg>
        <span>www.brightpath.io</span>
      </li>
    </ul>

    <div class="name-band">
      <p class="person-name">OMAR SALEH</p>
      <p class="person-role">OWNER</p>
    </div>

    <p class="address">P. O. Box 4120, Dammam 32415<br>Saudi Arabia</p>
  </section>

</body>
</html>
```